A Freight forwarding (transportation/shipping) company requires stationary design

We need The following:
1. Letterhead
2. Letter Envelope
3. A4 Paper Envelope
4. A4 Paper Folder (One that is 2xA4 foldable size which we can open in half and we can put a paper in between)
5. A5 Paper (To be used for notes taking)

a design for a freight forwarding company named BORUMAND TALAJ INTERNATIONAL TRANSPORTATION CO . Business Card is already designed and should follow it, the files attached help guide you in type of docs required + Logos (We are active in Sea Transportation, Truck transportation, and Air Transportation, (printed design is required with all open source files for editing - lamination accepted)

The said company is agent and sales representative of 2 other Shipping companies (whose logos, name, and website should also be mentioned on Envelopes and Folder) - Velor Tide and QMD Shipping, logos attached.

Velor Tide Shipping LLC
Dubai, United Arab Emirates
www.vtduae-example.com

QMD Shipping Line Ltd
London, United Kingdom
www.qmdfleet-example.com

Address is "No.8, 2nd Sadaf Kuy-e-Nilufari, Tehran, IR
Tel number is +98 21 55402913
Fax number is +98 21 55406287
E-Mail address is info@borumandtalaj-example.com
Website is www.borumandtalaj-example.com

```html
<!DOCTYPE html>
<html lang="en">
<head>
<meta charset="utf-8">
<title>Borumand Talaj – Stationery Set</title>
<link href="https://fonts.googleapis.com/css2?family=Open+Sans:wght@400;600;700&display=swap" rel="stylesheet">
<style>
:root{
  --bg:#6b6b6b;
  --paper:#f4f3f1;
  --navy:#123f5e;
  --blue:#4391d0;
  --ink:#3b3b3b;
  --muted:#6a6a6a;
  --rule:#9a9a9a;
  --partner-light:#5cb5e4;
}
*{box-sizing:border-box;margin:0;padding:0}
html,body{width:1200px;height:944px;overflow:hidden;background:var(--bg);font-family:"Open Sans",Arial,sans-serif;color:var(--ink)}
.canvas{position:relative;width:1200px;height:944px}
.sheet{position:absolute;background:var(--paper);overflow:hidden}
.band{position:absolute;left:0;right:0;bottom:0;height:10px;display:block}

/* brand name block standing for the mark */
.brand{position:absolute;display:flex;flex-direction:column;align-items:center;text-align:center;color:var(--navy);font-weight:600}
.brand .dot{border-radius:50%;background:var(--navy);margin-bottom:4px}
.brand .name{line-height:1.2}
.brand.sm .dot{width:30px;height:30px}
.brand.sm .name{font-size:5px;width:60px}
.brand.xs .dot{width:22px;height:22px}
.brand.xs .name{font-size:3.8px;width:46px}
.brand.light{color:#fff}
.brand.light .dot{background:#fff}
.brand.lg .dot{width:70px;height:70px;margin-bottom:10px}
.brand.lg .name{font-size:8px;width:130px;font-weight:700}

.contact{position:absolute;border-left:1px solid #b9b9b9;font-size:7px;line-height:9px;color:var(--ink)}
.contact .row{display:flex;align-items:center;gap:4px}
.contact svg{width:6px;height:6px;fill:var(--navy);flex:none}

/* letterhead */
.letterhead{left:29px;top:22px;width:345px;height:486px}
.letterhead .greeting{position:absolute;left:35px;top:137px;font-size:9.5px}
.letterhead .body{position:absolute;left:35px;top:165px;width:277px;font-size:4.8px;line-height:6.8px;color:var(--muted)}
.letterhead .body p{margin-bottom:6px;text-align:justify}
.letterhead .closing{position:absolute;left:35px;top:340px;font-size:5px;color:var(--muted)}
.letterhead .sign{position:absolute;left:38px;top:350px;width:50px;height:20px}
.letterhead .signer{position:absolute;left:37px;top:376px;font-size:5.5px;line-height:6.5px;color:var(--muted)}

/* envelopes */
.flap{position:absolute;left:0;right:0;top:0}
.flap-mark{position:absolute;border-radius:50%;border:2px solid #fff}
.partner{position:absolute;text-align:center;font-size:4.6px;line-height:6px;color:var(--muted)}
.partner .tag{display:flex;align-items:center;justify-content:center;gap:4px;font-weight:700;font-size:7px;margin-bottom:3px}
.partner .tag i{display:block;width:14px;height:14px;border-radius:50%}
.partner .url{margin-top:5px;letter-spacing:.5px;font-size:4.8px}
.qmd .tag{color:var(--partner-light)} .qmd .tag i{background:var(--partner-light)} .qmd .url{color:var(--partner-light)}
.vtd .tag{color:var(--navy)} .vtd .tag i{background:var(--navy)} .vtd .url{color:var(--navy)}

.a4-envelope{left:394px;top:26px;width:307px;height:482px;background:transparent}
.a4-envelope .body-panel{position:absolute;left:0;right:0;top:52px;bottom:0;background:var(--paper)}

.dl-back{left:720px;top:138px;width:386px;height:174px}
.dl-mid{left:766px;top:229px;width:387px;height:175px;box-shadow:-2px 2px 6px rgba(0,0,0,.15)}
.dl-front{left:720px;top:332px;width:387px;height:176px;box-shadow:-2px 2px 6px rgba(0,0,0,.2)}

/* notepads */
.pad{top:568px;width:240px;height:332px}
.pad.lined .lines{position:absolute;left:13px;right:13px;top:75px;height:218px;
  background:repeating-linear-gradient(to bottom,transparent 0 14.3px,var(--rule) 14.3px 15.3px)}
.pad-a{left:50px}
.pad-b{left:331px}
.pad-c{left:609px;background:linear-gradient(160deg,#1f4d6e,var(--navy) 60%)}
.pad-d{left:886px;background:linear-gradient(160deg,#5aa2da,var(--blue) 60%)}
.pad .foot{position:absolute;left:0;right:0;bottom:16px;text-align:center;font-size:4.4px;line-height:6px;color:var(--muted)}
.pad .foot b{font-weight:700}
.pad .site{position:absolute;left:0;right:0;bottom:26px;text-align:center;color:#fff;font-size:7.4px;letter-spacing:2.6px}
</style>
</head>
<body>
<main class="canvas">

  <!-- Letterhead -->
  <section class="sheet letterhead" aria-label="Letterhead">
    <div class="brand sm" style="left:22px;top:38px"><span class="dot"></span><span class="name">Borumand Talaj International Transportation Co</span></div>
    <div class="contact" style="left:206px;top:38px;padding-left:11px">
      <div>No.8, 2nd Sadaf</div>
      <div>Kuy-e-Nilufari, Tehran, IR</div>
      <div class="row"><svg viewBox="0 0 10 10"><path d="M2 0l2 2-1 2a6 6 0 0 0 3 3l2-1 2 2-2 2C4 10 0 6 0 2z"/></svg>+98 21 55402913</div>
      <div class="row"><svg viewBox="0 0 10 10"><rect x="0" y="3" width="10" height="5"/><rect x="2" y="0" width="6" height="3"/></svg>+98 21 55406287</div>
      <div class="row"><svg viewBox="0 0 10 10"><path d="M0 2h10v6H0z M0 2l5 3 5-3" /></svg>info@borumandtalaj-example.com</div>
      <div class="row"><svg viewBox="0 0 10 10"><circle cx="5" cy="5" r="5"/></svg>www.borumandtalaj-example.com</div>
    </div>
    <div class="greeting">Dear Mr. Aldren,</div>
    <div class="body">
      <p>Lorem ipsum dolor sit amet, consectetur adipiscing elit. Donec orci purus, luctus vitae dignissim eu, iaculis sed purus. Vivamus faucibus, ipsum nec aliquet viverra, leo mauris condimentum ligula, sit amet sagittis enim ligula quis arcu. Nam egestas tortor id nisi porttitor mattis. In tortor ante, ultricies in suscipit a, tempus non massa.</p>
      <p>Donec malesuada orci vitae nulla accumsan porta a id massa. Quisque accumsan iaculis magna sit amet fringilla. Maecenas consequat, magna eget tincidunt semper, odio nibh rutrum mi, id feugiat ante nisi eu risus. Vestibulum nunc orci, rhoncus a placerat in, ultricies in mi.</p>
      <p>Sed id augue vitae urna euismod commodo aliquet a quam. Pellentesque arcu velit, cursus et malesuada ut, consequat et diam. Nullam erat sem, rhoncus id ullamcorper vitae, rhoncus et arcu. In ultricies ultricies nulla, ut rutrum nisi iaculis at. Donec eu magna a metus ornare faucibus.</p>
      <p>It is a long established fact that a reader will be distracted by the readable content of a page when looking at its layout, making it look like readable English.</p>
    </div>
    <div class="closing">Sincerely,</div>
    <svg class="sign" viewBox="0 0 50 20"><path d="M2 8c8-4 14-3 10 2s10-4 16-2-4 6 0 6 12-4 20-4" fill="none" stroke="#222" stroke-width="1"/></svg>
    <div class="signer">Peter Aldren<br>CEO/ Founder</div>
    <svg class="band" viewBox="0 0 345 10" preserveAspectRatio="none"><path d="M0 4H282L288 0H345V10H0Z" fill="var(--navy)"/><path d="M0 2H282" stroke="var(--navy)" stroke-width=".6"/></svg>
  </section>

  <!-- A4 envelope -->
  <section class="sheet a4-envelope" aria-label="A4 paper envelope">
    <svg class="flap" width="307" height="54" viewBox="0 0 307 54"><path d="M0 54L10 10Q12 0 24 0H283Q295 0 297 10L307 54Z" fill="var(--navy)"/></svg>
    <div class="flap-mark" style="left:144px;top:12px;width:20px;height:20px"></div>
    <div class="body-panel">
      <div class="brand sm" style="left:22px;top:22px"><span class="dot"></span><span class="name">Borumand Talaj International Transportation Co</span></div>
      <div class="partner qmd" style="left:12px;top:367px;width:100px"><div class="tag"><i></i>QMD Shipping</div>QMD Shipping Line Ltd<br>London, United Kingdom<div class="url">www.qmdfleet-example.com</div></div>
      <div class="partner vtd" style="left:196px;top:367px;width:100px"><div class="tag"><i></i>Velor Tide</div>Velor Tide Shipping LLC<br>Dubai, United Arab Emirates<div class="url">www.vtduae-example.com</div></div>
      <svg class="band" viewBox="0 0 307 10" preserveAspectRatio="none"><path d="M0 4H244L250 0H307V10H0Z" fill="var(--navy)"/><path d="M0 2H244" stroke="var(--navy)" stroke-width=".6"/></svg>
    </div>
  </section>

  <!-- Letter envelopes -->
  <section class="sheet dl-back" aria-label="Letter envelope back, light blue flap">
    <svg class="flap" width="386" height="64" viewBox="0 0 386 64"><path d="M0 0H386L380 50Q378 64 362 64H24Q8 64 6 50Z" fill="var(--blue)"/></svg>
    <div class="flap-mark" style="left:181px;top:27px;width:22px;height:22px"></div>
  </section>
  <section class="sheet dl-mid" aria-label="Letter envelope back, navy flap">
    <svg class="flap" width="387" height="66" viewBox="0 0 387 66"><path d="M0 0H387L381 52Q379 66 363 66H24Q8 66 6 52Z" fill="var(--navy)"/></svg>
    <div class="flap-mark" style="left:182px;top:28px;width:22px;height:22px"></div>
  </section>
  <section class="sheet dl-front" aria-label="Letter envelope front">
    <div class="brand sm" style="left:14px;top:23px"><span class="dot"></span><span class="name">Borumand Talaj International Transportation Co</span></div>
    <div class="partner qmd" style="left:6px;top:117px;width:100px"><div class="tag"><i></i>QMD Shipping</div>QMD Shipping Line Ltd<br>London, United Kingdom<div class="url">www.qmdfleet-example.com</div></div>
    <div class="partner vtd" style="left:280px;top:117px;width:100px"><div class="tag"><i></i>Velor Tide</div>Velor Tide Shipping LLC<br>Dubai, United Arab Emirates<div class="url">www.vtduae-example.com</div></div>
    <svg class="band" viewBox="0 0 387 10" preserveAspectRatio="none"><path d="M0 4H322L328 0H387V10H0Z" fill="var(--navy)"/><path d="M0 2H322" stroke="var(--navy)" stroke-width=".6"/></svg>
  </section>

  <!-- Notepads -->
  <section class="sheet pad lined pad-a" aria-label="A5 notepad with contact header">
    <div class="brand xs" style="left:12px;top:22px"><span class="dot"></span><span class="name">Borumand Talaj International Transportation Co</span></div>
    <div class="contact" style="left:152px;top:24px;padding-left:7px;font-size:5px;line-height:6.2px">
      <div>No.8, 2nd Sadaf</div>
      <div>Kuy-e-Nilufari, Tehran, IR</div>
      <div class="row"><svg viewBox="0 0 10 10"><path d="M2 0l2 2-1 2a6 6 0 0 0 3 3l2-1 2 2-2 2C4 10 0 6 0 2z"/></svg>+98 21 55402913</div>
      <div class="row"><svg viewBox="0 0 10 10"><rect x="0" y="3" width="10" height="5"/><rect x="2" y="0" width="6" height="3"/></svg>+98 21 55406287</div>
      <div class="row"><svg viewBox="0 0 10 10"><path d="M0 2h10v6H0z"/></svg>info@borumandtalaj-example.com</div>
      <div class="row"><svg viewBox="0 0 10 10"><circle cx="5" cy="5" r="5"/></svg>www.borumandtalaj-example.com</div>
    </div>
    <div class="lines"></div>
    <svg class="band" style="height:6px" viewBox="0 0 240 6" preserveAspectRatio="none"><path d="M0 3H190L194 0H240V6H0Z" fill="var(--navy)"/></svg>
  </section>

  <section class="sheet pad lined pad-b" aria-label="A5 notepad with footer contact">
    <div class="brand xs" style="left:97px;top:24px"><span class="dot"></span><span class="name">Borumand Talaj International Transportation Co</span></div>
    <div class="lines"></div>
    <div class="foot"><b>A:</b> No.8, 2nd Sadaf, Kuy-e-Nilufari, Tehran, IR <b>P:</b> +98 21 55402913<br><b>F:</b> +98 21 55406287 <b>E:</b> info@borumandtalaj-example.com <b>W:</b> borumandtalaj-example.com</div>
    <svg class="band" style="height:6px" viewBox="0 0 240 6" preserveAspectRatio="none"><path d="M0 3H190L194 0H240V6H0Z" fill="var(--navy)"/></svg>
  </section>

  <section class="sheet pad pad-c" aria-label="Notepad cover, navy">
    <div class="brand lg light" style="left:55px;top:110px"><span class="dot"></span><span class="name">Borumand Talaj International Transportation Co</span></div>
    <div class="site">www.borumandtalaj-example.com</div>
  </section>

  <section class="sheet pad pad-d" aria-label="Notepad cover, blue">
    <div class="brand lg light" style="left:55px;top:110px"><span class="dot"></span><span class="name">Borumand Talaj International Transportation Co</span></div>
    <div class="site">www.borumandtalaj-example.com</div>
  </section>

</main>
</body>
</html>
```